PowerPoint template for project mangement course material

I need a ppt template for the slides at our project management course. IT should be arather simple adn stylish not taking the focus away from the content. We are two companies delivering the course - thus the template should be held in the colours of the two companies and their logos. we need different layouts for the template - the logos should be included in minimum the title layout.
The content is a mix of text and figures.
(uploaded ppt shows an example of the content)

Industry/Entity Type

Training

Font styles to use
Serif
Sans Serif

Requirements
Must have
• different layouts: title, section, standard, two columns, headline only etc.
Nice to have
• nice bullets, mostly white background

```html
<!DOCTYPE html>
<html lang="en">
<head>
<meta charset="utf-8">
<title>Project Management Course – Slide Template</title>
<link rel="stylesheet" href="https://fonts.googleapis.com/css2?family=Lato:ital,wght@0,300;0,400;0,700;1,400&family=Noto+Serif:wght@400&display=swap">
<style>
:root{
  --stage:#000;
  --paper:#fafafa;
  --blue:#4d73a3;
  --blue-light:#6d8fba;
  --navy:#1b4270;
  --footer:#173d66;
  --red:#a53331;
  --grey:#666;
  --grey-dark:#555;
  --grey-light:#e4e4e4;
  --text:#888;
  --ink:#333;
  --sans:'Lato',sans-serif;
  --serif:'Noto Serif',serif;
}
*{margin:0;padding:0;box-sizing:border-box}
html,body{width:1200px;height:717px;overflow:hidden;background:var(--stage)}
.deck{position:relative;width:1200px;height:717px;font-family:var(--sans)}
.slide{position:absolute;width:384px;height:220px;background:var(--paper);overflow:hidden}
.c1{left:12px}.c2{left:409px}.c3{left:806px}
.r1{top:19px}.r2{top:250px}.r3{top:481px}
.abs{position:absolute}
.footer{position:absolute;left:0;bottom:0;width:100%;height:12px;background:var(--footer);color:#fff;font-size:5px;line-height:12px;padding-left:4px}
.page-no{position:absolute;right:6px;top:0;height:12px;width:16px;background:var(--grey-dark);text-align:center;font-size:5px}
.brand{position:absolute;top:8px;right:8px;display:flex;align-items:center;gap:5px;font-size:6px;color:var(--grey-dark)}
.brand .divider{width:1px;height:16px;background:#ccc}
.brand .dot{display:inline-block;width:5px;height:5px;border-radius:50%;background:var(--navy);margin-right:2px;vertical-align:middle}
.slide-title{position:absolute;left:12px;top:14px;font-size:11px;font-weight:300;color:var(--navy)}
.slide-title em{font-style:normal;font-weight:400}
.slide-title.under::after{content:"";position:absolute;left:0;bottom:-4px;width:14px;height:2px;background:var(--red)}
.slide-title.bar{padding-left:8px}
.slide-title.bar::before{content:"";position:absolute;left:-12px;top:-3px;width:4px;height:20px;background:var(--red)}
.slide-title.bar.grey::before{background:#bbb}
.body{font-size:4.5px;line-height:1.85;color:var(--text)}
.just{text-align:justify}
.ph{position:absolute}
/* title slide */
.hero{left:0;top:0;width:384px;height:155px;background:linear-gradient(160deg,#6f92bd 0%,var(--blue) 55%,#3f6696 100%)}
.hero-title{left:0;width:384px;top:60px;text-align:center;color:#fff;font-family:var(--serif);font-size:23px}
.hero-sub{left:54px;width:276px;top:92px;text-align:center;color:#fff;font-family:var(--serif);font-size:7px;line-height:1.7}
.title-brand{position:absolute;left:0;width:384px;top:172px;display:flex;justify-content:center;align-items:center;gap:10px;font-size:12px;color:var(--grey-dark)}
.title-brand .divider{width:1px;height:28px;background:#ccc}
.title-brand .dot{display:inline-block;width:9px;height:9px;border-radius:50%;background:var(--navy);margin-right:3px;vertical-align:middle}
.footer.red{background:var(--red);display:flex;justify-content:space-between;padding:0 6px;font-family:var(--serif)}
/* welcome */
.portrait-round{left:162px;top:53px;width:60px;height:60px;border-radius:50%;border:1px solid #ddd;background:radial-gradient(circle at 50% 40%,#d9d9d9,#9a9a9a)}
.name-red{color:var(--red);font-weight:700;font-size:6.5px}
/* ceo */
.quote{left:94px;top:154px;width:265px;height:44px;background:#6e6e6e;color:#fff;font-style:italic;font-size:5.6px;line-height:1.8;padding:5px 10px}
/* section */
.section-band{left:0;top:30px;width:384px;height:178px;background:linear-gradient(170deg,#6a8cb7,var(--blue) 60%,#46699a)}
.section-title{left:0;width:384px;top:98px;text-align:center;color:#fff;font-size:18px;font-weight:700}
.section-sub{left:50px;width:284px;top:125px;text-align:center;color:#fff;font-size:5.2px;line-height:1.75}
/* rows */
.row-title{font-size:7.5px;font-weight:700;color:var(--navy)}
.row-title::after{content:"";display:block;width:10px;height:1.5px;background:var(--red);margin-top:3px}
.big-no{font-size:32px;font-weight:700;color:#e9e9e9;line-height:1}
.block{left:0;width:123px;height:43px}
.block .no{position:absolute;right:2px;top:6px;font-size:33px;font-weight:700;color:rgba(255,255,255,.18);line-height:1}
.sub-head{font-size:6.8px;font-weight:700;color:var(--navy)}
.sub-head.red{color:var(--red)}
.circle{width:68px;height:68px;border-radius:50%;color:rgba(255,255,255,.7);font-size:8.5px;font-weight:700;display:flex;align-items:center;justify-content:center;text-align:center;line-height:1.2}
</style>
</head>
<body>
<main class="deck">

  <!-- Title layout -->
  <section class="slide c1 r1">
    <div class="ph hero" role="img" aria-label="Full-width blue-tinted background photograph"></div>
    <h1 class="abs hero-title">Project Title Here</h1>
    <p class="abs hero-sub">Liquorice chupa chups applicake apple pie cupcake brownie bear claw cake gingerbread cotton candy. Bear claw croissant apple pie. Croissant cake sweet puff oreo .</p>
    <div class="title-brand"><span>Nordvik Partners</span><span class="divider"></span><span><span class="dot"></span>Halvo Consulting</span></div>
    <footer class="footer red"><span>Copyright text here</span><span>Author Name Here</span><span>www.halvo-example.com</span></footer>
  </section>

  <!-- Welcome message -->
  <section class="slide c2 r1">
    <h2 class="slide-title under">Welcome <em>Message !</em></h2>
    <div class="brand"><span>Nordvik Partners</span><span class="divider"></span><span><span class="dot"></span>Halvo</span></div>
    <div class="ph portrait-round" role="img" aria-label="Round portrait photo of the employee"></div>
    <p class="abs name-red" style="left:0;width:384px;top:121px;text-align:center">EMPLOYEE NAME</p>
    <p class="abs" style="left:0;width:384px;top:130px;text-align:center;font-size:5px;color:var(--ink)">Company Name</p>
    <p class="abs body" style="left:28px;top:141px;width:340px">Liquorice chupa chups applicake apple pie cupcake brownie bear claw cake gingerbread cotton candy. Bear claw croissant apple pie. Croissant cake sweet puff oreo . Liquorice chupa chups applicake apple pie cupcake brownie bear claw cake gingerbread cotton candy. Bear claw croissant apple pie. Croissant cake sweet puff oreo. Liquorice chupa chups applicake apple pie cupcake brownie bear claw cake gingerbread cotton candy. Bear claw croissant apple pie.</p>
    <p class="abs body" style="left:28px;top:183px;width:340px">Liquorice chupa chups applicake apple pie cupcake brownie bear claw cake gingerbread cotton candy. Bear claw croissant apple pie. Croissant cake sweet puff oreo . Liquorice chupa chups applicake</p>
    <footer class="footer">Copyright text here<span class="page-no">01</span></footer>
  </section>

  <!-- CEO message -->
  <section class="slide c3 r1">
    <h2 class="slide-title">CEO <em>Message !</em></h2>
    <div class="brand"><span>Nordvik Partners</span><span class="divider"></span><span><span class="dot"></span>Halvo</span></div>
    <div class="ph" style="left:0;top:36px;width:140px;height:172px;background:linear-gradient(180deg,#e8e8e8,#8a8a8a)" role="img" aria-label="Black-and-white photo of the CEO"></div>
    <p class="abs" style="left:152px;top:56px;font-size:8px;font-weight:700;color:var(--red);border-left:1.5px solid var(--red);padding-left:4px;line-height:1">Emplyoee Name</p>
    <p class="abs" style="left:158px;top:68px;font-size:5px;color:var(--grey)">Designation</p>
    <p class="abs body" style="left:158px;top:86px;width:200px">Liquorice chupa chups applicake apple pie cupcake brownie bear claw cake gingerbread cotton candy. Bear claw croissant apple pie. Croissant cake sweet puff oreo . Liquorice chupa chups applicake apple pie cupcake brownie bear claw cake gingerbread cotton candy. Bear claw croissant apple pie. Croissant cake sweet puff oreo. Liquorice chupa chups applicake apple pie cupcake brownie bear claw cake gingerbread cotton candy. Bear claw croissant apple pie.</p>
    <p class="abs quote">“ Liquorice chupa chups applicake apple pie cupcake brownie bear claw cake ginger bread cotton candy. Bear claw croissant apple pie. Croissant cake sweet puff oreo . Liquorice chupa chups applicake ”</p>
    <footer class="footer">Copyright text here<span class="page-no">01</span></footer>
  </section>

  <!-- Section divider -->
  <section class="slide c1 r2">
    <div class="brand"><span>Nordvik Partners</span><span class="divider"></span><span><span class="dot"></span>Halvo</span></div>
    <div class="ph section-band" role="img" aria-label="Blue-tinted background photograph"></div>
    <h2 class="abs section-title">SECTION DIVIDER HERE</h2>
    <p class="abs section-sub">Liquorice chupa chups applicake apple pie cupcake brownie bear claw cake gingerbread cotton candy. Bear claw croissant apple pie. Croissant cake sweet puff oreo . Liquorice chupa chups applicake apple pie cupcake brownie bear claw</p>
    <footer class="footer">Copyright text here<span class="page-no">01</span></footer>
  </section>

  <!-- Products: image + text -->
  <section class="slide c2 r2">
    <div class="brand"><span>Nordvik Partners</span><span class="divider"></span><span><span class="dot"></span>Halvo</span></div>
    <div class="ph" style="left:0;top:0;width:213px;height:208px;background:linear-gradient(150deg,#cfd6df,#f2f2f2 55%,#9fb4cc)" role="img" aria-label="Photo of hands reviewing printed charts with a pen"></div>
    <h2 class="abs" style="left:234px;top:47px;font-size:11px;font-weight:400;color:var(--red)">OUR PRODUCTS</h2>
    <p class="abs body just" style="left:234px;top:67px;width:130px;font-size:5px;line-height:2.2">Liquorice chupa chups applicake apple pie cupcake brownie bear claw cake gingerbread cotton candy. Bear claw croissant apple pie. Croissant cake sweet puff oreo . Liquorice chupa chups applicake apple pie cupcake brownie bear claw cake gingerbread cotton candy. Bear claw croissant apple pie. Croissant cake sweet puff oreo. Liquorice chupa chups applicake apple pie cupcake brownie bear claw cake gingerbread cotton candy.</p>
    <footer class="footer">Copyright text here<span class="page-no">01</span></footer>
  </section>

  <!-- Figure + text -->
  <section class="slide c3 r2">
    <div class="brand"><span>Nordvik Partners</span><span class="divider"></span><span><span class="dot"></span>Halvo</span></div>
    <div class="ph" style="left:0;top:0;width:218px;height:164px;background:linear-gradient(160deg,#e6eef7,#8fb0d8 60%,#3f73b8)" role="img" aria-label="Photo of a blue bar chart printout"></div>
    <div class="ph" style="left:0;top:164px;width:218px;height:44px;background:var(--red)"></div>
    <p class="abs" style="left:12px;top:171px;width:200px;color:#fff;font-size:4.8px;line-height:1.8">Liquorice chupa chups applicake apple pie cupcake brownie bear claw cake gingerbread cotton candy. Liquorice chupa chups applicake apple pie cupcake brownie bear claw cake gingerbread cotton candy.</p>
    <p class="abs body just" style="left:236px;top:54px;width:128px;font-size:6px;line-height:1.85">Liquorice chupa chups applicake apple pie cupcake brownie bear claw cake gingerbread cotton candy. Bear claw croissant apple pie. Croissant cake sweet puff oreo . Liquorice chupa chups applicake apple pie cupcake brownie bear claw cake gingerbread cotton candy. Bear claw croissant apple pie. Croissant cake sweet puff oreo. Liquorice chupa chups applicake apple pie cupcake brownie bear claw cake gingerbread cotton candy.</p>
    <footer class="footer">Copyright text here<span class="page-no">01</span></footer>
  </section>

  <!-- Numbered sections -->
  <section class="slide c1 r3">
    <h2 class="slide-title bar grey">Main <em>Title Here</em></h2>
    <div class="brand"><span>Nordvik Partners</span><span class="divider"></span><span><span class="dot"></span>Halvo</span></div>
    <div class="abs" style="left:126px;top:45px;width:1px;height:155px;background:#ddd"></div>
    <p class="abs big-no" style="left:80px;top:56px">01</p>
    <p class="abs big-no" style="left:80px;top:112px">02</p>
    <p class="abs big-no" style="left:80px;top:168px">03</p>
    <h3 class="abs row-title" style="left:18px;top:47px">Section Title Here</h3>
    <h3 class="abs row-title" style="left:18px;top:101px">Section Title Here</h3>
    <h3 class="abs row-title" style="left:18px;top:157px">Section Title Here</h3>
    <p class="abs body" style="left:137px;top:45px;width:240px">Liquorice chupa chups applicake apple pie cupcake brownie bear claw cake gingerbread cotton candy. Bear claw croissant apple pie. Croissant cake sweet puff oreo . Liquorice chupa chups applicake apple pie cupcake brownie bear claw cake gingerbread cotton candy. Bear claw croissant apple pie. Croissant cake sweet puff oreo.</p>
    <p class="abs body" style="left:137px;top:99px;width:240px">Liquorice chupa chups applicake apple pie cupcake brownie bear claw cake gingerbread cotton candy. Bear claw croissant apple pie. Croissant cake sweet puff oreo . Liquorice chupa chups applicake apple pie cupcake brownie bear claw cake gingerbread cotton candy. Bear claw croissant apple pie. Croissant cake sweet puff oreo.</p>
    <p class="abs body" style="left:137px;top:155px;width:240px">Liquorice chupa chups applicake apple pie cupcake brownie bear claw cake gingerbread cotton candy. Bear claw croissant apple pie. Croissant cake sweet puff oreo . Liquorice chupa chups applicake apple pie cupcake brownie bear claw cake gingerbread cotton candy. Bear claw croissant apple pie. Croissant cake sweet puff oreo.</p>
    <footer class="footer">Copyright text here<span class="page-no">01</span></footer>
  </section>

  <!-- Coloured blocks -->
  <section class="slide c2 r3">
    <h2 class="slide-title bar" style="font-size:12px;color:var(--red)">Our <em style="color:var(--navy)">Products</em></h2>
    <div class="brand"><span>Nordvik Partners</span><span class="divider"></span><span><span class="dot"></span>Halvo</span></div>
    <div class="abs block" style="top:43px;background:var(--navy)"><span class="no">01</span></div>
    <div class="abs block" style="top:99px;background:var(--red)"><span class="no">02</span></div>
    <div class="abs block" style="top:155px;background:var(--grey-dark)"><span class="no">03</span></div>
    <div class="abs" style="left:123px;top:43px;width:1px;height:155px;background:#ddd"></div>
    <p class="abs body" style="left:137px;top:45px;width:240px">Liquorice chupa chups applicake apple pie cupcake brownie bear claw cake gingerbread cotton candy. Bear claw croissant apple pie. Croissant cake sweet puff oreo . Liquorice chupa chups applicake apple pie cupcake brownie bear claw cake gingerbread cotton candy. Bear claw croissant apple pie. Croissant cake sweet puff oreo.</p>
    <p class="abs body" style="left:137px;top:99px;width:240px">Liquorice chupa chups applicake apple pie cupcake brownie bear claw cake gingerbread cotton candy. Bear claw croissant apple pie. Croissant cake sweet puff oreo . Liquorice chupa chups applicake apple pie cupcake brownie bear claw cake gingerbread cotton candy. Bear claw croissant apple pie. Croissant cake sweet puff oreo.</p>
    <footer class="footer">Copyright text here<span class="page-no">01</span></footer>
  </section>

  <!-- Services -->
  <section class="slide c3 r3">
    <h2 class="slide-title bar" style="color:var(--navy)">Our <em>Services</em></h2>
    <div class="brand"><span>Nordvik Partners</span><span class="divider"></span><span><span class="dot"></span>Halvo</span></div>
    <h3 class="abs sub-head" style="left:22px;top:45px">PRODUCT SUBTEXT HERE</h3>
    <p class="abs body" style="left:22px;top:55px;width:250px;line-height:1.9">Liquorice chupa chups applicake apple pie cupcake brownie bear claw cake gingerbread cotton candy. Bear claw croissant apple pie. Croissant cake sweet puff oreo . Liquorice chupa chups applicake apple pie cupcake brownie bear claw cake gingerbread cotton candy. Bear claw croissant apple pie. Croissant cake sweet puff oreo. Liquorice chupa chups applicake apple pie cupcake brownie bear claw cake gingerbread cotton candy. Bear claw croissant apple pie. Croissant cake sweet puff oreo. Liquorice chupa chups applicake apple pie cupcake brownie bear claw cake gingerbread cotton candy.</p>
    <h3 class="abs sub-head red" style="left:22px;top:123px">PRODUCT SUBTEXT HERE</h3>
    <p class="abs body" style="left:22px;top:133px;width:250px;line-height:1.9">Liquorice chupa chups applicake apple pie cupcake brownie bear claw cake gingerbread cotton candy. Bear claw croissant apple pie. Croissant cake sweet puff oreo . Liquorice chupa chups applicake apple pie cupcake brownie bear claw cake gingerbread cotton candy. Bear claw croissant apple pie. Croissant cake sweet puff oreo. Liquorice chupa chups applicake apple pie cupcake brownie bear claw cake gingerbread cotton candy. Bear claw croissant apple pie. Croissant cake sweet puff oreo. Liquorice chupa chups applicake apple pie cupcake brownie bear claw cake gingerbread cotton candy.</p>
    <div class="abs circle" style="left:290px;top:45px;background:var(--navy)">IMAGE<br>HERE</div>
    <div class="abs circle" style="left:290px;top:128px;background:var(--red)">IMAGE<br>HERE</div>
    <footer class="footer">Copyright text here<span class="page-no">01</span></footer>
  </section>

</main>
</body>
</html>
```